web site update

I want to get a better website for a small high end remodeling and construction company
I currently have a web site but you will find that it is not good.
www.quenbrickhall.com
We are a high end construction / remodeling company that has been in business since 2003. We primarily work in the mid peninsula of the bay area. Most of our clientele are very educated captains of industry. This group is still the target client.
I had my logo designed by Mint Easel a few years ago and I do like it, I like the orange and black or orange a blue. I don’t have a lot of content on hand as far as professional photographs.
Number of pages not sure and are open to: design pages vs full function website
I think what I am after is a web presence that will seal the deal as we are getting high referrals from past clients.
Construction
1 page

```html
<!DOCTYPE html>
<html lang="en">
<head>
<meta charset="utf-8">
<title>Quenbrick Hall Remodeling – Contact Us</title>
<link rel="stylesheet" href="https://fonts.googleapis.com/css2?family=Open+Sans:wght@400;600;700;800&display=swap">
<style>
:root{
  --orange:#f26a0f;
  --black:#000;
  --ink:#111;
  --page:#fff;
  --frame:#e6e6e6;
  --field:#efefef;
  --field-text:#666;
  --rule:#555;
  --dark-field:#2b2b2b;
}
*{box-sizing:border-box;margin:0;padding:0}
html,body{width:1025px;height:1200px;overflow:hidden;background:var(--frame);font-family:"Open Sans",Arial,sans-serif}
.page{position:absolute;left:13px;top:13px;width:999px;height:1174px;background:var(--page)}
.brand{position:absolute;left:30px;top:40px;display:flex;align-items:center;gap:12px}
.brand-mark{width:26px;height:26px;background:var(--orange)}
.brand-name{font-weight:800;font-size:22px;color:var(--orange);letter-spacing:.5px;line-height:1.05}
.taglines{position:absolute;right:26px;top:21px;display:flex;gap:22px}
.tagline{display:flex;align-items:center;gap:5px;color:var(--orange);font-weight:700;font-size:15px}
.tagline svg{width:19px;height:19px}
.header-email{position:absolute;right:27px;top:72px;display:flex;align-items:center;gap:9px;font-size:21px;color:var(--ink)}
.header-email svg{width:37px;height:37px}
.main-nav{position:absolute;left:0;top:128px;width:999px;height:38px;background:var(--orange);display:flex;padding-left:278px}
.main-nav a{color:#fff;text-decoration:none;font-weight:700;font-size:14px;line-height:38px;padding:0 34px}
.main-nav a.active{background:var(--black)}
.hero{position:absolute;left:0;top:166px;width:999px;height:346px;background:linear-gradient(100deg,#4a3a2a 0%,#8c6a45 35%,#c9a36f 60%,#d8bb8a 100%)}
.contact-title{position:absolute;left:0;top:556px;width:999px;text-align:center;font-size:23px;font-weight:600;color:var(--ink)}
.contact-form .field{position:absolute;background:var(--field);border:0;font-family:inherit;font-size:12.5px;color:var(--field-text);padding:9px 15px}
.f-name{left:239px;top:610px;width:256px;height:32px}
.f-email{left:239px;top:651px;width:256px;height:32px}
.f-phone{left:239px;top:692px;width:256px;height:32px}
.f-message{left:504px;top:610px;width:256px;height:74px}
.send{position:absolute;left:504px;top:692px;width:90px;height:33px;background:var(--black);color:#fff;font-weight:600;font-size:13px;text-align:center;line-height:33px}
.footer{position:absolute;left:0;top:792px;width:999px;height:348px}
.footer svg.roof{position:absolute;left:0;top:0}
.footer-name{position:absolute;left:0;top:50px;width:999px;text-align:center;color:#fff;font-weight:700;font-size:13px;letter-spacing:1px}
.col{position:absolute;top:134px}
.col h3{color:#fff;font-size:14px;font-weight:700;padding-bottom:6px;border-bottom:1px solid var(--rule);margin-bottom:14px}
.quick{left:53px;width:108px}
.quick a{display:block;color:#fff;text-decoration:none;font-size:12px;font-weight:600;line-height:20px}
.mapcol{left:219px;width:263px}
.map{width:263px;height:145px;background:linear-gradient(135deg,#e8e4da,#d9d6cc 60%,#ebe2b2)}
.details{left:542px;width:176px}
.detail{display:flex;gap:10px;color:#fff;font-size:12px;font-weight:600;line-height:18px;margin-bottom:16px}
.detail svg{flex:none;width:26px;height:26px}
.follow{left:776px;width:173px}
.social{display:flex;gap:4px;margin-bottom:18px}
.social span{width:24px;height:24px;border-radius:50%;background:var(--orange)}
.news-input{height:25px;background:var(--dark-field);color:#aaa;font-size:10px;padding:5px 12px;margin-bottom:10px}
.subscribe{display:inline-block;background:var(--dark-field);color:#fff;font-weight:700;font-size:12px;padding:5px 13px}
.copyright{position:absolute;left:0;top:1148px;width:999px;text-align:center;font-size:10.5px;font-weight:600;color:#333}
</style>
</head>
<body>
<div class="page">
  <header>
    <div class="brand"><span class="brand-mark"></span><span class="brand-name">QUENBRICK HALL<br>REMODELING</span></div>
    <div class="taglines">
      <span class="tagline"><svg viewBox="0 0 20 20"><circle cx="10" cy="10" r="9" fill="none" stroke="var(--orange)" stroke-width="1.5"/><circle cx="10" cy="10" r="6.5" fill="var(--orange)"/><path d="M7 10h6M10.5 7.5 13 10l-2.5 2.5" stroke="#fff" stroke-width="1.6" fill="none"/></svg>LISTEN BETTER</span>
      <span class="tagline"><svg viewBox="0 0 20 20"><circle cx="10" cy="10" r="9" fill="none" stroke="var(--orange)" stroke-width="1.5"/><circle cx="10" cy="10" r="6.5" fill="var(--orange)"/><path d="M7 10h6M10.5 7.5 13 10l-2.5 2.5" stroke="#fff" stroke-width="1.6" fill="none"/></svg>PLAN BETTER</span>
      <span class="tagline"><svg viewBox="0 0 20 20"><circle cx="10" cy="10" r="9" fill="none" stroke="var(--orange)" stroke-width="1.5"/><circle cx="10" cy="10" r="6.5" fill="var(--orange)"/><path d="M7 10h6M10.5 7.5 13 10l-2.5 2.5" stroke="#fff" stroke-width="1.6" fill="none"/></svg>BUILD BETTER</span>
    </div>
    <div class="header-email"><svg viewBox="0 0 38 38"><circle cx="19" cy="19" r="17.5" fill="#fff" stroke="#000" stroke-width="2"/><rect x="10" y="12.5" width="18" height="13" fill="#000"/><path d="M10.5 13l8.5 7 8.5-7M10.5 25l6-6M27.5 25l-6-6" stroke="#fff" stroke-width="1.3" fill="none"/></svg>office@quenbrickhall.com</div>
    <nav class="main-nav"><a href="#">HOME</a><a href="#">SERVICES</a><a href="#" class="active">CONTACT US</a><a href="#">MAKE PAYMENT</a></nav>
  </header>
  <div class="hero" role="img" aria-label="Photo of two builders in hard hats and safety vests on a framing site"></div>
  <h1 class="contact-title">Contact Us</h1>
  <div class="contact-form">
    <div class="field f-name">Name</div>
    <div class="field f-email">Email</div>
    <div class="field f-phone">Phone</div>
    <div class="field f-message">Message</div>
    <div class="send">SEND</div>
  </div>
  <footer class="footer">
    <svg class="roof" width="999" height="348" viewBox="0 0 999 348"><polygon points="0,90 499.5,16 999,90 999,348 0,348" fill="var(--black)"/><polyline points="0,90 499.5,16 999,90" fill="none" stroke="var(--orange)" stroke-width="5"/></svg>
    <div class="footer-name">QUENBRICK HALL</div>
    <div class="col quick"><h3>QUICK LINKS</h3><a href="#">&gt; HOME</a><a href="#">&gt; SERVICES</a><a href="#">&gt; CONTACT US</a><a href="#">&gt; MAKE PAYMENT</a></div>
    <div class="col mapcol"><h3>LOCATION MAP</h3><div class="map" role="img" aria-label="Street map showing the office location"></div></div>
    <div class="col details"><h3>CONTACT DETAILS</h3>
      <div class="detail"><svg viewBox="0 0 26 26"><circle cx="13" cy="13" r="13" fill="var(--orange)"/><path d="M13 6a4.5 4.5 0 0 0-4.5 4.5C8.5 14 13 20 13 20s4.5-6 4.5-9.5A4.5 4.5 0 0 0 13 6z" fill="#fff"/><circle cx="13" cy="10.5" r="1.7" fill="var(--orange)"/></svg><span>418 Alder Crest Ave<br>Palo Alto, CA 94301</span></div>
      <div class="detail"><svg viewBox="0 0 26 26"><circle cx="13" cy="13" r="13" fill="var(--orange)"/><path d="M8.5 7.5l2.5-.5 1.5 3.5-1.5 1.2a8 8 0 0 0 3.3 3.3l1.2-1.5 3.5 1.5-.5 2.5c-6 .5-10.5-4-10-10z" fill="#fff"/></svg><span style="line-height:26px">650.555.0142</span></div>
      <div class="detail"><svg viewBox="0 0 26 26"><circle cx="13" cy="13" r="13" fill="var(--orange)"/><rect x="7" y="8.5" width="12" height="9" fill="#fff"/><path d="M7.5 9l5.5 4.5L18.5 9" stroke="var(--orange)" stroke-width="1.2" fill="none"/></svg><span style="line-height:26px">office@quenbrickhall.com</span></div>
    </div>
    <div class="col follow"><h3>FOLLOW US</h3>
      <div class="social"><span></span><span></span><span></span></div>
      <h3>NEWSLETTER</h3>
      <div class="news-input">Email</div>
      <div class="subscribe">SUBSCRIBE</div>
    </div>
  </footer>
  <div class="copyright">© 2016 QUENBRICK HALL REMODELING. ALL RIGHTS RESERVED.</div>
</div>
</body>
</html>
```